Wine Bottle Label for the brand Gliding Heron for a Sherry wine

A wine label for a Dry Sherry. We want it consistent with existing Gliding Heron and Quiet Otter labeling. It should say "Quiet Otter Sherry" We want a very retro look similar to the attached labels which are from our core wines. The sherry is a side project that fits into the 'quiet otter' series (label included). We would like a lot of the similar label structure to the existing quiet otter label, but with a different caricature of the fox. We have had one that we did in Copper ridge bourbon barrels and the caricature was of a buffalo with a barrel imbibing. We have also had a giraffe on a skin contact white. I have included the mural and other logos throughout the project to give you a sense of the previous work we have done.

Industry/Entity Type

Winemaking, wine labels

Requirements
Must have
• Quiet Otter elements

```html
<!DOCTYPE html>
<html lang="en">
<head>
<meta charset="utf-8">
<title>Quiet Otter Sherry – Label</title>
<link rel="stylesheet" href="https://fonts.googleapis.com/css2?family=Alfa+Slab+One&family=Cinzel&family=Lobster&family=Montserrat:wght@400;600;700&family=Oswald:wght@500&display=swap">
<style>
  :root {
    --backdrop: #2a1016;
    --paper-light: #f2dc98;
    --paper-dark: #d2aa5e;
    --ink: #151010;
    --accent-red: #e9524b;
    --frame-white: #ffffff;
    --ornament: #2b2118;
  }
  * { margin: 0; padding: 0; box-sizing: border-box; }
  html, body { width: 1200px; height: 1070px; overflow: hidden; background: var(--backdrop); }
  .canvas { position: relative; width: 1200px; height: 1070px; background: var(--backdrop); }
  .label { position: absolute; left: 290px; top: 65px; width: 620px; height: 940px; }
  .label-shape { position: absolute; inset: 0; }
  .label-text { position: absolute; left: 0; width: 620px; text-align: center; color: var(--ink); font-family: "Montserrat", sans-serif; }
  .district { top: 70px; font-size: 17px; font-weight: 600; line-height: 22px; }
  .house-name { top: 146px; font-family: "Alfa Slab One", serif; font-size: 62px; color: var(--accent-red); letter-spacing: 1px; line-height: 70px; }
  .rule { position: absolute; height: 3px; background: var(--ink); }
  .rule-top { left: 114px; width: 392px; top: 222px; }
  .rule-bottom { left: 144px; width: 330px; top: 722px; height: 2px; }
  .name-box { position: absolute; left: 200px; top: 250px; width: 220px; height: 216px; border: 3px solid var(--accent-red); outline: 1px solid var(--accent-red); outline-offset: -9px; display: flex; flex-direction: column; justify-content: center; align-items: center; }
  .name-box span { font-family: "Oswald", sans-serif; font-weight: 500; font-size: 80px; line-height: 88px; color: var(--accent-red); letter-spacing: 3px; }
  .ornament { position: absolute; top: 240px; width: 140px; height: 258px; border-radius: 40px; background: radial-gradient(ellipse at center, rgba(43,33,24,0.55), rgba(43,33,24,0.08) 70%); }
  .ornament-left { left: 46px; }
  .ornament-right { left: 433px; }
  .product { top: 482px; font-family: "Cinzel", serif; font-size: 48px; line-height: 56px; }
  .bottled-by { top: 546px; font-size: 20px; font-weight: 700; letter-spacing: 4px; color: var(--accent-red); }
  .producer { top: 578px; font-family: "Lobster", cursive; font-size: 46px; line-height: 54px; letter-spacing: 1px; }
  .town { top: 645px; font-size: 19px; font-weight: 700; letter-spacing: 5px; color: var(--accent-red); }
  .contents { position: absolute; top: 680px; left: 144px; width: 336px; display: flex; justify-content: space-between; align-items: center; font-family: "Montserrat", sans-serif; font-weight: 700; font-size: 13px; line-height: 16px; color: var(--ink); }
  .contents .center { text-align: center; }
  .imported { top: 730px; font-size: 19px; font-weight: 600; line-height: 26px; color: var(--accent-red); }
  .address { top: 788px; font-size: 15px; line-height: 21px; }
  .printed { top: 858px; font-size: 11px; font-weight: 700; }
</style>
</head>
<body>
<main class="canvas">
  <section class="label" aria-label="Quiet Otter Sherry label">
    <svg class="label-shape" width="620" height="940" viewBox="0 0 620 940" aria-hidden="true">
      <defs>
        <path id="label-outline" d="M40 240 Q40 0 310 0 Q580 0 580 240 A40 40 0 0 0 620 280 L620 680 A40 40 0 0 0 580 720 Q580 940 310 940 Q40 940 40 720 A40 40 0 0 0 0 680 L0 280 A40 40 0 0 0 40 240 Z"/>
        <radialGradient id="paper" cx="50%" cy="45%" r="60%">
          <stop offset="0%" stop-color="var(--paper-light)"/>
          <stop offset="100%" stop-color="var(--paper-dark)"/>
        </radialGradient>
      </defs>
      <use href="#label-outline" fill="var(--frame-white)" stroke="var(--ink)" stroke-width="4"/>
      <use href="#label-outline" fill="none" stroke="var(--ink)" stroke-width="2.5" transform="translate(310 470) scale(0.965) translate(-310 -470)"/>
      <use href="#label-outline" fill="var(--ink)" transform="translate(310 470) scale(0.935) translate(-310 -470)"/>
      <use href="#label-outline" fill="var(--frame-white)" transform="translate(310 470) scale(0.925) translate(-310 -470)"/>
      <use href="#label-outline" fill="url(#paper)" transform="translate(310 470) scale(0.905) translate(-310 -470)"/>
    </svg>

    <p class="label-text district">BOTTLED IN THE<br>SHERRY DISTRICT</p>
    <h1 class="label-text house-name">REALEZA</h1>
    <div class="rule rule-top"></div>

    <div class="ornament ornament-left" role="img" aria-label="Decorative floral flourish"></div>
    <div class="name-box"><span>QUIET</span><span>OTTER</span></div>
    <div class="ornament ornament-right" role="img" aria-label="Decorative floral flourish"></div>

    <h2 class="label-text product">SHERRY</h2>
    <p class="label-text bottled-by">PRODUCT &amp; BOTTLED BY</p>
    <p class="label-text producer">Vinalta, S. L.</p>
    <p class="label-text town">JEREZ DE LA FRONTERA</p>

    <div class="contents">
      <span>CONTENTS:<br>1 PINT. 7 FL. OZS.</span>
      <span class="center">2200</span>
      <span>20% ALCOHOL<br>BY VOLUME</span>
    </div>
    <div class="rule rule-bottom"></div>

    <p class="label-text imported">IMPORTED BY<br>NORTHGATE SPIRITS CO., INC.</p>
    <p class="label-text address">14, Harbor Lane St,<br>Basic Permit, N.0 2-K-48<br>New Haven, Connecticut,</p>
    <p class="label-text printed">PRINTED IN SPAIN</p>
  </section>
</main>
</body>
</html>
```